Create an Engaging Yet Simple Cycle Infographic to be featured in new book

I require a clearly designed, simple to navigate infographic. It will depict a "CYCLE-style" Framework that includes 7-stages which are underpinned by 6-enablers. The cycle is the core concept of a new business book. Each component also needs a simple graphic/ icon that can be used as a short-cut to identify the specific stage or enabler. The attached brief provides further details.

Target Market(s)

Business leaders

Font styles to use
Serif

Colors
000000

Requirements
Must have
• Simple, easy to engage with, fit on portrait-oriented book page

```html
<!DOCTYPE html>
<html lang="en">
<head>
<meta charset="utf-8">
<title>Organisation Growth &amp; Thriving</title>
<link href="https://fonts.googleapis.com/css2?family=Tinos:wght@400;700&family=Arimo:wght@400;700&display=swap" rel="stylesheet">
<style>
  :root {
    --ink: #000000;
    --paper: #ffffff;
    --panel-light: #f4f4f4;
    --panel-dark: #d2d2d2;
    --text-dark: #1a1a1a;
  }
  * { box-sizing: border-box; margin: 0; padding: 0; }
  html, body { width: 849px; height: 1200px; overflow: hidden; background: var(--paper); }
  .infographic { position: relative; width: 849px; height: 1200px; font-family: "Arimo", Arial, sans-serif; color: var(--ink); }

  .title {
    position: absolute; left: 28px; right: 28px; top: 34px;
    font-family: "Tinos", "Times New Roman", serif; font-weight: 700;
    font-size: 50px; text-align: center; letter-spacing: 0.5px;
    padding-bottom: 10px; border-bottom: 4px solid var(--ink);
  }

  .diagram { position: absolute; left: 0; top: 0; }

  .stage-note {
    position: absolute; left: 28px; width: 272px; height: 92px;
    display: flex; align-items: center; padding: 0 34px 0 14px;
    font-size: 17.5px; line-height: 1.25; color: var(--text-dark);
    background: linear-gradient(90deg, var(--panel-light), var(--panel-dark));
    clip-path: polygon(0 0, 88% 0, 100% 50%, 88% 100%, 0 100%);
  }

  .stage-label {
    position: absolute; left: 296px; width: 112px;
    text-align: center; color: var(--paper);
    font-weight: 700; font-size: 15px; line-height: 1.3; transform: translateY(-50%);
  }

  .enabler {
    position: absolute; left: 450px; width: 340px; height: 64px;
    background: var(--ink); border-radius: 32px;
    display: flex; align-items: center; padding-left: 22px;
    color: var(--paper); font-size: 19px; line-height: 1.15;
  }
  .enabler-name { width: 220px; }
  .enabler-icon {
    position: absolute; right: -8px; top: 50%; transform: translateY(-50%);
    width: 92px; height: 92px; border-radius: 50%; background: var(--ink);
    display: flex; align-items: center; justify-content: center;
  }
  .icon-placeholder { width: 58px; height: 58px; border-radius: 50%; background: var(--paper); }

  .legend {
    position: absolute; top: 1040px; height: 82px;
    background: var(--ink); color: var(--paper); border-radius: 50%;
    display: flex; align-items: center; justify-content: center;
    font-family: "Tinos", "Times New Roman", serif; font-size: 30px; letter-spacing: 1px;
  }
  .legend-stages { left: 226px; width: 246px; }
  .legend-enablers { left: 488px; width: 256px; }
</style>
</head>
<body>
<main class="infographic">
  <h1 class="title">Organisation Growth &amp; Thriving</h1>

  <svg class="diagram" width="849" height="1200" viewBox="0 0 849 1200" aria-hidden="true">
    <polygon points="352,148 418,196 402,196 402,1022 302,1022 302,196 286,196" fill="var(--ink)"/>
    <g stroke="var(--paper)" stroke-width="3">
      <line x1="302" y1="291" x2="402" y2="291"/>
      <line x1="302" y1="411" x2="402" y2="411"/>
      <line x1="302" y1="533" x2="402" y2="533"/>
      <line x1="302" y1="658" x2="402" y2="658"/>
      <line x1="302" y1="781" x2="402" y2="781"/>
      <line x1="302" y1="903" x2="402" y2="903"/>
    </g>
  </svg>

  <div class="stage-note" style="top:184px">Make the journey from where we are today, to where we need to be</div>
  <div class="stage-note" style="top:305px">Set the destination and plan how to get there</div>
  <div class="stage-note" style="top:426px">Set design- criteria and use them to explore choose options</div>
  <div class="stage-note" style="top:550px">Choose to take action and make the necessary trade-offs</div>
  <div class="stage-note" style="top:674px">Take time to understand the real opportunity or problem</div>
  <div class="stage-note" style="top:796px">See the change and recognise it to be relevant/ worth noticing</div>
  <div class="stage-note" style="top:918px">Reflect on improvement opportunities and apply them next time</div>

  <div class="stage-label" style="top:232px">MOVE TO IT</div>
  <div class="stage-label" style="top:352px">PLAN IT</div>
  <div class="stage-label" style="top:472px">DESIGN IT</div>
  <div class="stage-label" style="top:596px">PRIORITISE IT</div>
  <div class="stage-label" style="top:720px">UNDERSTAND IT</div>
  <div class="stage-label" style="top:842px">SEE IT</div>
  <div class="stage-label" style="top:964px">LEARN FROM IT</div>

  <div class="enabler" style="top:242px">
    <span class="enabler-name">Balanced Ecosystem</span>
    <span class="enabler-icon">
      <svg width="60" height="60" viewBox="0 0 60 60" aria-hidden="true">
        <circle cx="30" cy="30" r="24" fill="none" stroke="var(--paper)" stroke-width="3"/>
        <ellipse cx="30" cy="30" rx="11" ry="24" fill="none" stroke="var(--paper)" stroke-width="3"/>
        <line x1="6" y1="30" x2="54" y2="30" stroke="var(--paper)" stroke-width="3"/>
        <line x1="10" y1="18" x2="50" y2="18" stroke="var(--paper)" stroke-width="2.5"/>
        <line x1="10" y1="42" x2="50" y2="42" stroke="var(--paper)" stroke-width="2.5"/>
      </svg>
    </span>
  </div>
  <div class="enabler" style="top:352px">
    <span class="enabler-name">Adaptive Leadership</span>
    <span class="enabler-icon"><span class="icon-placeholder" role="img" aria-label="Icon of a group with raised arms"></span></span>
  </div>
  <div class="enabler" style="top:466px">
    <span class="enabler-name">The Golden Thread</span>
    <span class="enabler-icon"><span class="icon-placeholder" role="img" aria-label="Icon of a spool of thread"></span></span>
  </div>
  <div class="enabler" style="top:584px">
    <span class="enabler-name">Anchors of Certainty</span>
    <span class="enabler-icon">
      <svg width="62" height="62" viewBox="0 0 62 62" aria-hidden="true">
        <circle cx="31" cy="31" r="28" fill="var(--paper)"/>
        <polyline points="17,32 27,42 46,21" fill="none" stroke="var(--ink)" stroke-width="7" stroke-linecap="round" stroke-linejoin="round"/>
      </svg>
    </span>
  </div>
  <div class="enabler" style="top:700px">
    <span class="enabler-name">Adaptive Mindset</span>
    <span class="enabler-icon"><span class="icon-placeholder" role="img" aria-label="Icon of a head with gears"></span></span>
  </div>
  <div class="enabler" style="top:820px">
    <span class="enabler-name">Enduring Commitment<br>(a core enabler)</span>
    <span class="enabler-icon"><span class="icon-placeholder" role="img" aria-label="Icon of a handshake"></span></span>
  </div>

  <div class="legend legend-stages">STAGES</div>
  <div class="legend legend-enablers">ENABLERS</div>
</main>
</body>
</html>
```